Dermavive Label Design

We need a label design for our cream dispenser. Its a cream against acne called Dermavive, Works with its active ingredients of silver and oxygen. We are looking for a flashy / colorful and modern design .
Updates

Low design quality

Target Market(s)

young people / People with acne

Industry/Entity Type

Skin Care Product

Colors

Designer to choose colors to be used in the design.

Requirements
Must have
• be modern, Colours
• -THE DESIGN NEEDS TO BE 10,7x7 , ITS 1 BIG STICKER THAT RAPS AROUND THE BOTTLE

```html
<!DOCTYPE html>
<html lang="en">
<head>
<meta charset="utf-8">
<title>Dermavive Acne Repair + Care Label</title>
<link rel="stylesheet" href="https://fonts.googleapis.com/css2?family=Questrial&family=Roboto:wght@500&display=swap">
<style>
  :root {
    --paper: #ffffff;
    --ink: #4a4f56;
    --ink-dark: #1f2226;
    --mist: #e6eef0;
    --teal-light: #a8dfe1;
    --teal: #36b6bb;
    --teal-deep: #1f9ca3;
    --silver-light: #f4f5f6;
    --silver-mid: #c9cdd1;
    --silver-dark: #80868c;
  }
  * { margin: 0; padding: 0; box-sizing: border-box; }
  html, body {
    width: 831px;
    height: 1200px;
    overflow: hidden;
    background: var(--paper);
  }
  .label {
    position: relative;
    width: 831px;
    height: 1200px;
    background: var(--paper);
    overflow: hidden;
  }
  .label__backdrop {
    position: absolute;
    left: 0;
    right: 0;
    top: 300px;
    bottom: 0;
    background: linear-gradient(to bottom,
      rgba(255,255,255,0) 0%,
      var(--mist) 14%,
      var(--teal-light) 38%,
      var(--teal) 62%,
      var(--teal-deep) 100%);
  }
  .maker {
    position: absolute;
    top: 70px;
    left: 0;
    right: 0;
    display: flex;
    justify-content: center;
    align-items: center;
    gap: 22px;
    font-family: "Questrial", sans-serif;
    font-size: 56px;
    line-height: 1;
    color: var(--ink);
  }
  .maker__square {
    width: 40px;
    height: 40px;
    border: 4px solid var(--ink);
  }
  .brand {
    position: absolute;
    top: 170px;
    left: 0;
    right: 0;
    text-align: center;
    font-family: "Questrial", sans-serif;
    font-weight: 400;
    font-size: 120px;
    line-height: 1.2;
    letter-spacing: 8px;
    color: var(--ink);
  }
  .claim {
    position: absolute;
    top: 460px;
    left: 55px;
    width: 720px;
    height: 200px;
    padding: 16px 0 0 48px;
    background: linear-gradient(to right, var(--silver-light) 0%, var(--silver-mid) 45%, var(--silver-light) 62%, var(--silver-dark) 100%);
    border: 2px solid var(--silver-mid);
    font-family: "Roboto", sans-serif;
    font-weight: 500;
    font-size: 70px;
    line-height: 84px;
    letter-spacing: 2px;
    color: var(--ink-dark);
  }
</style>
</head>
<body>
  <main class="label">
    <div class="label__backdrop" role="img" aria-label="Teal halftone dot pattern with floating bubbles, fading up into white"></div>

    <div class="maker">
      <span class="maker__square"></span>
      <span class="maker__name">Lumora Labs</span>
    </div>

    <h1 class="brand">Dermavive</h1>

    <p class="claim">ACNE<br>REPAIR + CARE</p>
  </main>
</body>
</html>
```